Boutique custom software development company needs new business card

Our nearly 20 year old custom software development company would like to better include the fact that we are now providing Bitcoin services. These new services are B2B include education (how to acquire and securely hold Bitcoin) and integrating Bitcoin payments into existing ecommerce sites or other existing systems. Please keep the card clean and simple. Attached is our current design and some other files. vexalon.example

Target Market(s)

businesses owners interested in long term relationship

Industry/Entity Type

Custom software development and Bitcoin

Contact Information for Business Card

Marcus Ellwood, marcus@vexalon.example, vexalon.example, (888) 555-VEXAL

Font styles to use
Other font styles liked:
• monospace

Requirements
Must have
• double-sided
Nice to have
• clean and simple
Should not have
• physical address

```html
<!DOCTYPE html>
<html lang="en">
<head>
<meta charset="utf-8">
<title>Vexalon Business Card</title>
<link href="https://fonts.googleapis.com/css2?family=Montserrat:wght@500;600;700;800&display=swap" rel="stylesheet">
<style>
  :root {
    --backdrop: #e4e5e6;
    --card-white: #ffffff;
    --brand-blue: #2f6fd6;
    --brand-blue-deep: #2152b0;
    --brand-orange: #f47b20;
    --ink: #2d3440;
    --shadow: rgba(0,0,0,0.18);
  }
  * { margin: 0; padding: 0; box-sizing: border-box; }
  html, body {
    width: 696px; height: 1200px; overflow: hidden;
    background: var(--backdrop);
    font-family: "Montserrat", Arial, sans-serif;
  }
  .canvas { position: relative; width: 696px; height: 1200px; }
  .card {
    position: absolute; left: 68px; width: 560px; height: 320px;
    box-shadow: 0 14px 30px var(--shadow);
    overflow: hidden;
  }
  .card--front { top: 200px; background: var(--card-white); }
  .card--back { top: 660px; background: var(--brand-blue); }

  .wordmark {
    position: absolute; font-weight: 800; letter-spacing: 0.5px; line-height: 1; white-space: nowrap;
  }
  .card--front .wordmark { left: 40px; top: 38px; font-size: 34px; color: var(--brand-blue); }
  .tagline {
    position: absolute; left: 41px; top: 77px;
    font-size: 9px; font-weight: 500; color: var(--brand-blue); letter-spacing: 0.3px; white-space: nowrap;
  }
  .holder-name {
    position: absolute; right: 60px; top: 92px;
    font-size: 17px; font-weight: 700; color: var(--brand-blue); letter-spacing: 0.5px; white-space: nowrap;
  }
  .contact {
    position: absolute; left: 40px; top: 150px;
    list-style: none; font-size: 12px; font-weight: 500; color: var(--ink); line-height: 20px;
  }
  .contact__item { display: flex; align-items: center; gap: 7px; white-space: nowrap; }
  .contact__icon { width: 9px; height: 9px; flex: none; }
  .corner-block {
    position: absolute; right: 0; bottom: 36px; width: 96px; height: 96px;
    background: var(--brand-blue);
  }
  .web-band {
    position: absolute; left: 0; right: 0; bottom: 0; height: 36px;
    background: var(--brand-orange);
    display: flex; align-items: center; padding-left: 40px;
    font-size: 12px; font-weight: 600; color: var(--card-white); letter-spacing: 0.3px;
  }

  .back-pattern {
    position: absolute; inset: 0;
    background: linear-gradient(135deg, var(--brand-blue) 0%, var(--brand-blue-deep) 100%);
  }
  .card--back .wordmark {
    left: 220px; top: 112px;
    font-size: 30px; color: var(--card-white);
  }
</style>
</head>
<body>
<main class="canvas">
  <section class="card card--front" aria-label="Card front">
    <div class="wordmark">VEXALON</div>
    <div class="tagline">custom software and bitcoin</div>
    <div class="holder-name">MARCUS ELLWOOD</div>
    <ul class="contact">
      <li class="contact__item">
        <svg class="contact__icon" viewBox="0 0 10 10"><circle cx="5" cy="5" r="4.5" fill="#f47b20"/></svg>
        (888) 555-VEXAL
      </li>
      <li class="contact__item">
        <svg class="contact__icon" viewBox="0 0 10 10"><circle cx="5" cy="5" r="4.5" fill="#f47b20"/></svg>
        502.555.0147
      </li>
      <li class="contact__item">
        <svg class="contact__icon" viewBox="0 0 10 10"><circle cx="5" cy="5" r="4.5" fill="#f47b20"/></svg>
        marcus@vexalon.example
      </li>
    </ul>
    <div class="corner-block" aria-hidden="true"></div>
    <div class="web-band">vexalon.example</div>
  </section>

  <section class="card card--back" aria-label="Card back">
    <div class="back-pattern" role="img" aria-label="Repeating brand pattern in shades of blue"></div>
    <div class="wordmark">VEXALON</div>
  </section>
</main>
</body>
</html>
```